Pop Album Cover - Front and Back, with Graphics Created

I am looking for someone to create a COMPLETE album cover, front and back, that I can get printed for CDs. All the details are in the document attached.

In general, for the front cover, there are 2 images that need to be composited, touched up, and designed with a bright background into one cover image graphic. There are other elements that need to be added as well, like the parental advisory warning and the record label logo, and some photoshopping so that the symbol on one of the clothing items in a picture is changed into a custom logo.

For the back cover, there is one image that needs to be designed to match the style of whatever you do for the front cover image, and then there is text information that needs to be added.

Between the two, and album "spine" is also needed - something simple with the name of the album: Melanie Tsao "NX"

All the images are included, along with the complete guide as a word document, below.

```html
<!DOCTYPE html>
<html lang="en">
<head>
<meta charset="utf-8">
<title>Melanie Tsao – NX album cover</title>
<link rel="stylesheet" href="https://fonts.googleapis.com/css2?family=Metal+Mania&family=Oswald:wght@500;600&display=swap">
<style>
  :root {
    --red: #d3141a;
    --red-bright: #ff2a22;
    --red-deep: #7a0508;
    --red-dark: #3a0204;
    --black: #0a0a0a;
    --white: #ffffff;
    --skin: #c9524a;
    --suit-white: #eeeaea;
  }
  * { margin: 0; padding: 0; box-sizing: border-box; }
  html, body { width: 1200px; height: 567px; overflow: hidden; background: var(--black); }
  .cover { position: relative; width: 1200px; height: 567px; overflow: hidden; }

  /* FRONT */
  .front {
    position: absolute; left: 0; top: 0; width: 550px; height: 567px;
    background: radial-gradient(ellipse at 45% 45%, var(--red-bright) 0%, var(--red) 45%, var(--red-deep) 100%);
  }
  .photo { position: absolute; }
  .photo--hero-white {
    left: 0; top: 0; width: 230px; height: 567px;
    background: linear-gradient(160deg, #1b1b1b 0%, var(--suit-white) 25%, #f7f7f7 55%, #b9b9b9 80%, rgba(200,200,200,0) 100%);
    clip-path: polygon(0 0, 62% 0, 100% 25%, 80% 55%, 40% 100%, 0 100%);
  }
  .photo--hero-black {
    left: 360px; top: 0; width: 190px; height: 567px;
    background: linear-gradient(175deg, var(--black) 0%, #1a1a1a 40%, #2a2a2a 60%, var(--black) 100%);
    clip-path: polygon(25% 0, 95% 0, 100% 100%, 10% 100%, 0 55%, 20% 35%);
  }
  .photo--portrait { left: 0; top: 0; width: 598px; height: 567px; }
  .artist-name {
    position: absolute; left: 92px; top: 164px;
    font-family: "Metal Mania", cursive; font-size: 34px; letter-spacing: 2px;
    color: var(--red); -webkit-text-stroke: 1.5px var(--black);
    text-shadow: 2px 2px 0 var(--black); white-space: nowrap;
  }
  .album-title {
    position: absolute; left: 118px; top: 185px;
    font-family: "Metal Mania", cursive; font-size: 230px; line-height: 1;
    color: var(--black); -webkit-text-stroke: 2px var(--red-deep);
    text-shadow: 3px 3px 0 var(--red-dark); transform: rotate(-4deg);
  }
  .advisory-badge {
    position: absolute; left: 18px; top: 519px; width: 50px; height: 38px;
    background: var(--white); border: 3px solid var(--black);
  }

  /* SPINE */
  .spine {
    position: absolute; left: 550px; top: 0; width: 52px; height: 567px;
    background: linear-gradient(90deg, #5a0306, var(--red) 50%, #5a0306);
  }
  .spine-title {
    position: absolute; left: 26px; top: 16px; width: 480px; height: 40px;
    transform-origin: 0 0; transform: rotate(90deg) translateY(-20px);
    font-family: "Metal Mania", cursive; font-size: 32px; line-height: 40px; letter-spacing: 3px;
    color: var(--red); -webkit-text-stroke: 1.5px var(--black);
    text-shadow: 2px 2px 0 var(--black); white-space: nowrap;
  }
  .spine-title .spine-album { margin-left: 50px; }

  .label-mark {
    position: absolute; display: flex; align-items: center; justify-content: center;
    background: var(--black);
    font-family: "Oswald", sans-serif; font-weight: 600; color: var(--red);
    text-align: center; line-height: 1;
  }
  .label-mark--front { left: 440px; top: 515px; width: 100px; height: 42px; font-size: 14px; }
  .label-mark--back { left: 1030px; top: 524px; width: 50px; height: 30px; font-size: 9px; }

  /* BACK */
  .back {
    position: absolute; left: 602px; top: 0; width: 598px; height: 567px;
    background: radial-gradient(ellipse at 55% 45%, var(--skin) 0%, #8e1a16 40%, var(--red-dark) 80%, #1a0102 100%);
  }
  .tracklist {
    position: absolute; left: 0; top: 82px; width: 598px; text-align: center;
    font-family: "Metal Mania", cursive; font-size: 30px; line-height: 46px;
    color: var(--white); letter-spacing: 2px; word-spacing: 8px;
    text-shadow: 2px 2px 0 var(--black);
  }
  .tracklist .num { color: var(--red); }
  .credits {
    position: absolute; left: 0; top: 396px; width: 640px; text-align: center;
    font-family: "Oswald", sans-serif; font-weight: 500; color: var(--white);
    font-size: 9.5px; line-height: 12px; text-transform: uppercase;
  }
  .credits .lead { font-size: 12.5px; line-height: 16px; font-weight: 600; }
  .credits .contact { margin-top: 8px; font-size: 10px; font-weight: 600; line-height: 12px; }
</style>
</head>
<body>
<div class="cover">

  <section class="front">
    <div class="photo photo--hero-white" role="img" aria-label="Photo of the singer in a white superhero costume with yellow glasses, leaping in from the left"></div>
    <div class="photo photo--hero-black" role="img" aria-label="Photo of the singer in a black masked superhero costume with utility belt, crouching on the right"></div>
    <div class="artist-name">MELANIE&nbsp;&nbsp;TSAO</div>
    <div class="album-title">NX</div>
    <div class="advisory-badge" aria-hidden="true"></div>
    <div class="label-mark label-mark--front">HALO KIT</div>
  </section>

  <section class="spine">
    <div class="spine-title">MELANIE&nbsp;&nbsp;TSAO<span class="spine-album">NX</span></div>
  </section>

  <section class="back">
    <div class="photo photo--portrait" role="img" aria-label="Close-up portrait of the singer in a black mask, tinted red"></div>
    <div class="tracklist">
      <span class="num">1.</span>STAR DRIFTER <span class="num">2.</span>NIGHTCAPE<br>
      <span class="num">3.</span>DAYDREAM GIRL <span class="num">4.</span>TOP SCORE <span class="num">5.</span>BRING IT
    </div>
    <div class="credits">
      <div class="lead">Produced by Rio Vance / Halo Kit Records</div>
      <div>Songs written and performed by Melanie Tsao</div>
      <div>All tracks recorded and mixed by Owen Prall / Tidewater Sound Recordings</div>
      <div>"Nightcape", "Top Score", "Star Drifter" mixed by Dean Collard</div>
      <div>"Daydream Girl", "Bring It" mixed by Ross Kemple / Wren Productions</div>
      <div>Cover:</div>
      <div>Photos by Levon Arakelian Photography</div>
      <div>Makeup by Nadia Ferro</div>
      <div>Costume pieces by Ellis Morrow &amp; Toby Grant</div>
      <div>Art by: ____________</div>
      <div class="contact">www.melanie-tsao.com<br>©2014 Halo Kit Records</div>
    </div>
  </section>
  <div class="label-mark label-mark--back">HALO KIT</div>

</div>
</body>
</html>
```